Product Labels - Background and Layout Refresh - Made in Australia

We require 2 labels designs to be updated. One for our premium Vantora brand and a second one for our standard quality Stelko brand.
We also require a new cover for our 2018 product catalog. Attached is the current design. We need an industrial type image in the background. Text to remain the same, fonts and textures can be changed.
Vantora: MI-001-1251-P+.ai
The old Brimvale product has been replaced with the new Vantora brand. Remove the brimvale logo and use the attached Vantora logo. Change background, fonts and layout. Use the made in Australia Logo or the words Made In Australia.
Stelko: MI-001-1251.ai
The logo remains the same, the background and the fonts are to be changed and updated.
Use made in Australia Logo or the words Made In Australia.
The text and diagram content must all remain on the labels.
The design theme needs to stay very industrial and rough.
Made in Australia is a big selling point for our products, ensure that message is conveyed on the labels.
Note: The size of the disc is 125mm the size of the label is now 85mm
The layer "Background" is to show how the final product will look. Refer to .jpg for details.
Target Market(s)
Industrial user of tools
Industry/Entity Type
Industrial
Colors
Designer to choose colors to be used in the design.
Requirements
Must have
- Industrial Feel & Emphasis on Made in Australia, by text, logo or other Images
Nice to have
- Trueforge Seal Logo
Should not have
- Not playful, not fun.

```html
<!DOCTYPE html>
<html lang="en">
<head>
<meta charset="utf-8">
<title>Kordex Brimvale – Catalogue Fabrication Products 2018</title>
<link rel="stylesheet" href="https://fonts.googleapis.com/css2?family=Montserrat:wght@300;700;800&display=swap">
<style>
  :root {
    --ink-white: #ffffff;
    --brand-amber: #c98a2b;
    --band-amber: rgba(150, 101, 28, 0.78);
    --steel-dark: #101010;
    --steel-mid: #4a4a4a;
    --steel-light: #9a9a9a;
  }
  html, body {
    margin: 0;
    padding: 0;
    overflow: hidden;
    background: var(--steel-dark);
  }
  .cover {
    position: relative;
    width: 927px;
    height: 1200px;
    overflow: hidden;
    font-family: "Montserrat", sans-serif;
    color: var(--ink-white);
  }
  .cover-photo {
    position: absolute;
    inset: 0;
    background:
      radial-gradient(ellipse 22% 40% at 50% 58%, rgba(200,200,200,0.55), transparent 70%),
      linear-gradient(90deg, rgba(0,0,0,0.55) 0%, transparent 30%, transparent 70%, rgba(0,0,0,0.55) 100%),
      linear-gradient(180deg, #1a1a1a 0%, var(--steel-mid) 22%, #5c5c5c 45%, var(--steel-mid) 70%, #161616 100%);
  }
  .brand {
    position: absolute;
    top: 30px;
    left: 0;
    width: 100%;
    display: flex;
    justify-content: center;
    align-items: center;
    gap: 18px;
  }
  .brand-mark {
    width: 62px;
    height: 62px;
    border-radius: 50%;
    border: 6px solid var(--brand-amber);
    box-sizing: border-box;
  }
  .brand-name {
    font-weight: 700;
    font-size: 34px;
    letter-spacing: 1px;
    color: var(--brand-amber);
    text-transform: uppercase;
  }
  .title-band {
    position: absolute;
    top: 318px;
    left: 0;
    width: 100%;
    height: 188px;
    background: var(--band-amber);
  }
  .title, .subtitle, .year {
    position: absolute;
    left: 0;
    width: 100%;
    margin: 0;
    text-align: center;
    line-height: 1;
    text-transform: uppercase;
  }
  .title {
    top: 326px;
    font-weight: 800;
    font-size: 112px;
    letter-spacing: -2px;
  }
  .subtitle {
    top: 435px;
    font-weight: 300;
    font-size: 53px;
    letter-spacing: 0;
  }
  .year {
    top: 502px;
    font-weight: 800;
    font-size: 142px;
    letter-spacing: -5px;
  }
</style>
</head>
<body>
  <main class="cover">
    <div class="cover-photo" role="img" aria-label="Black and white photo of a long warehouse aisle lined with steel shelving under a mesh ceiling, with an angle grinder throwing sparks in the foreground"></div>

    <header class="brand">
      <span class="brand-mark" aria-hidden="true"></span>
      <span class="brand-name">Kordex Brimvale</span>
    </header>

    <div class="title-band" aria-hidden="true"></div>
    <h1 class="title">Catalogue</h1>
    <p class="subtitle">Fabrication Products</p>
    <p class="year">2018</p>
  </main>
</body>
</html>
```